Verdant Orchard - Stationery Design Project

We need a stationary for our business. We grow roots and fruits in Central and South America, we import and distribute in FL, USA. We do fresh and frozen products.

Target Market(s)

Small and big supermarkets, wholesalers, traders, distributors, etc

Industry/Entity Type

Business

```html
<!DOCTYPE html>
<html lang="en">
<head>
<meta charset="utf-8">
<title>Verdant Orchard Group – Stationery</title>
<link rel="stylesheet" href="https://fonts.googleapis.com/css2?family=Questrial&display=swap">
<style>
  :root {
    --orange: #e8821f;
    --green: #556334;
    --peach: #f6c9a0;
    --peach-light: #f7dcc2;
    --ink: #2e2e2e;
    --paper: #ffffff;
    --backdrop: #ffffff;
  }
  * { margin: 0; padding: 0; box-sizing: border-box; }
  html, body { width: 1200px; height: 900px; overflow: hidden; background: var(--backdrop); }
  body { font-family: "Questrial", "Century Gothic", sans-serif; color: var(--ink); }
  .canvas { position: relative; width: 1200px; height: 900px; }

  .sheet {
    position: absolute;
    background: var(--paper);
    box-shadow: 2px 3px 8px rgba(0,0,0,.35);
    overflow: hidden;
  }

  /* Letterhead */
  .letterhead { left: 58px; top: 32px; width: 586px; height: 828px; }
  .wordmark {
    position: absolute;
    color: var(--green);
    font-weight: 400;
    letter-spacing: .5px;
    white-space: nowrap;
    display: flex; align-items: center; gap: 8px;
  }
  .wordmark .dot { width: 12px; height: 12px; border-radius: 50%; background: var(--green); }
  .letterhead .wordmark { left: 39px; top: 88px; font-size: 25px; }
  .flourish {
    position: absolute;
    background: radial-gradient(ellipse at center, rgba(246,201,160,.75) 0%, rgba(246,201,160,.35) 55%, rgba(246,201,160,0) 75%);
  }
  .flourish-top { left: 295px; top: 20px; width: 280px; height: 260px; border-radius: 40% 10% 50% 50%; }
  .flourish-bottom { left: 18px; top: 550px; width: 330px; height: 260px; border-radius: 50% 50% 40% 10%; }

  .letter { position: absolute; left: 97px; top: 140px; width: 393px; font-size: 10px; line-height: 14.5px; }
  .letter p { margin: 0; }
  .letter .date { margin-bottom: 27px; }
  .letter .meta { margin-bottom: 27px; }
  .letter .salutation { margin-bottom: 27px; }
  .letter .body { text-align: justify; margin-bottom: 16px; letter-spacing: -.1px; }
  .letter .closing { margin-top: 62px; }
  .letter .signature { margin-top: 14px; }
  .letter-footer { position: absolute; left: 212px; top: 700px; color: var(--orange); }
  .letter-footer .address { font-size: 10px; margin-bottom: 6px; }
  .letter-footer .contact { font-size: 8px; }

  /* Envelope front */
  .envelope-front { left: 693px; top: 167px; width: 440px; height: 278px; }
  .envelope-front .wordmark { left: 34px; top: 32px; font-size: 15px; }
  .envelope-front .wordmark .dot { width: 8px; height: 8px; }
  .leaf-art {
    position: absolute; left: 0; top: 55px; width: 440px; height: 223px;
    background: linear-gradient(160deg, var(--peach-light) 0%, rgba(247,220,194,.85) 60%, rgba(247,220,194,.4) 100%);
    clip-path: polygon(0 0, 20% 30%, 45% 70%, 70% 45%, 100% 40%, 100% 100%, 0 100%);
  }

  /* Envelope back */
  .envelope-back { left: 697px; top: 493px; width: 432px; height: 297px; }
  .fruit-pattern { position: absolute; left: 0; top: 0; width: 432px; height: 160px; }
  .fruit-pattern .band-orange { height: 82px; background: var(--orange); }
  .fruit-pattern .band-green { height: 78px; background: var(--green); }
  .pocket { position: absolute; left: 0; top: 0; width: 432px; height: 297px; }
</style>
</head>
<body>
<main class="canvas">

  <section class="sheet letterhead" aria-label="Letterhead">
    <div class="flourish flourish-top" role="img" aria-label="Peach floral scroll ornament in the top right corner"></div>
    <div class="flourish flourish-bottom" role="img" aria-label="Peach floral scroll ornament in the bottom left corner"></div>

    <div class="wordmark"><span class="dot"></span>VERDANT ORCHARD GROUP</div>

    <div class="letter">
      <p class="date">Date</p>
      <p class="meta">Title<br>Motto<br>Offices</p>
      <p class="salutation">To whom it may concern,</p>
      <p class="body">Lorem ipsum dolor sit amet, consectetur adipisicing elit, sed do eiusmod tempor incididunt ut labore et dolore magna aliqua. Ut enim ad minim veniam, quis nostrud exercitation ullamco laboris nisi ut aliquip ex ea commodo consequat. Duis aute irure dolor in reprehenderit in voluptate velit esse cillum dolore eu fugiat nulla pariatur. Excepteur sint occaecat cupidatat non proident, sunt in culpa qui officia deserunt mollit anim id est laborum. S</p>
      <p class="body">ed ut perspiciatis unde omnis iste natus error sit voluptatem accusantium doloremque laudantium, totam rem aperiam, eaque ipsa quae ab illo inventore veritatis et quasi architecto beatae vitae dicta sunt explicabo. Nemo enim ipsam voluptatem quia voluptas sit aspernatur aut odit aut fugit, sed quia consequuntur magni dolores eos qui ratione voluptatem sequi nesciunt.</p>
      <p class="body">Neque porro quisquam est, qui dolorem ipsum quia dolor sit amet, consectetur, adipisci velit, sed quia non numquam eius modi tempora incidunt ut labore et dolore magnam aliquam quaerat voluptatem.</p>
      <p class="closing">Sincerely,</p>
      <p class="signature">Verdant Orchard Group</p>
    </div>

    <footer class="letter-footer">
      <p class="address">Offices Address XXX - XXXX - XXX</p>
      <p class="contact">Tel. +(00) 000 000 | Email hello@verdantorchard.com | Fax +(00) 000 000 000</p>
    </footer>
  </section>

  <section class="sheet envelope-front" aria-label="Envelope front">
    <div class="leaf-art" role="img" aria-label="Large pale peach leaf shapes rising from the bottom edge"></div>
    <div class="wordmark"><span class="dot"></span>VERDANT ORCHARD GROUP</div>
  </section>

  <section class="sheet envelope-back" aria-label="Envelope back">
    <div class="fruit-pattern" role="img" aria-label="White fruit silhouette pattern on orange and olive green bands">
      <div class="band-orange"></div>
      <div class="band-green"></div>
    </div>
    <svg class="pocket" viewBox="0 0 432 297" aria-hidden="true">
      <path d="M0 297 V140 Q0 128 14 128 H418 Q432 128 432 140 V297 Z" fill="#ffffff"/>
      <path d="M6 297 V142 Q6 134 16 134 H416 Q426 134 426 142" fill="none" stroke="#bdbdbd" stroke-width="1"/>
    </svg>
  </section>

</main>
</body>
</html>
```